We need a new menu with more professional outlook for our restaurant called Bo Tien Golden Vegetarian Cuisine. We are vegetarian restaurant offered healthy food with nice environment and service. Our restaurant's pictures and take away menu are available on www.botien-eatery.example.au. I want to redesign our eat in and take away menu to be similar to our restaurant's theme and something which is green, healthy and professional. I gave the menu of my favorite restaurant on Google Docs.
Dear all,
Industry/Entity Type
Environment
Requirements
Must have
- I am really interested in the design and layout of the restaurant in our local area- please refer to these files: https://files.example.net/open?id=7K-QwertyZpLmNbVcXzAsDfGhJkLq and https://files.example.net/open?id=7K-QwertyZpLmRtYuIoPaSdFgHjKw . We would like something look like this: simple, easy to follow and professional.

```html
<!DOCTYPE html>
<html lang="en">
<head>
<meta charset="utf-8">
<title>Bo Tien Golden Vegetarian Cuisine – Menu</title>
<link rel="stylesheet" href="https://fonts.googleapis.com/css2?family=Tinos:wght@400;700&family=Arimo:wght@400&family=Russo+One&display=swap">
<style>
:root{
  --bg:#0f3a1d;
  --panel:#ffffff;
  --dish:#1d561c;
  --price:#e08a00;
  --band:#e8930a;
  --lime:#8fd21e;
  --pale:#e4e4e4;
  --note-bg:#474747;
}
*{box-sizing:border-box;margin:0;padding:0}
html,body{width:1200px;height:855px;overflow:hidden}
body{background:var(--bg);font-family:"Tinos",serif;position:relative}
.panel{position:absolute;background:var(--panel);border-radius:16px}
.panel-left{left:10px;top:24px;width:376px;height:820px;padding:20px 10px 0 15px}
.panel-specials{left:413px;top:24px;width:367px;height:335px;padding:20px 10px 0 13px}
.panel-rice{left:413px;top:373px;width:367px;height:166px;padding:13px 12px 0 13px}
.panel-banquet{left:413px;top:546px;width:367px;height:294px;padding:12px 12px 0 12px}
.dish{display:grid;grid-template-columns:1fr 46px;column-gap:6px;margin-bottom:10.5px;line-height:11.5px;font-size:10.6px;color:#1a1a1a}
.dish-name{color:var(--dish);text-transform:uppercase}
.dish-price{color:var(--price);text-align:left}
.dish-desc{grid-column:1/2}
.panel-specials .dish{margin-bottom:10.8px;grid-template-columns:1fr 42px}
.panel-rice .dish{margin-bottom:5.5px;grid-template-columns:1fr 42px}
.section-band{background:var(--band);color:#fff;font-family:"Arimo",sans-serif;font-size:15px;height:28px;line-height:28px;padding-left:13px;border-radius:5px;margin:0 2px 10px 0}
.panel-left .section-band{margin:28px 0 14px 0}
.banquet-set{text-align:center;text-transform:uppercase;font-weight:700;color:var(--dish);font-size:10.4px;line-height:16.7px}
.banquet-set .set-price{color:var(--price);font-weight:400}
.banquet-set + .banquet-set{margin-top:16px}
.brand{position:absolute;left:830px;top:150px;width:330px;text-align:center}
.brand-name{font-family:"Tinos",serif;font-weight:700;color:var(--band);font-size:30px;line-height:34px}
.brand-tag{font-family:"Arimo",sans-serif;color:var(--lime);font-size:14px;margin-top:8px}
.info{position:absolute;left:830px;top:296px;width:330px;text-align:center;font-family:"Arimo",sans-serif;color:var(--pale);font-size:15px;line-height:18.6px}
.tagline{font-family:"Russo One",sans-serif;color:var(--band);font-size:19px;line-height:23px;letter-spacing:1px;margin:6px 0 15px}
.gst{color:var(--band)}
.gap{height:17px}
.promises{position:absolute;left:830px;top:588px;width:330px;text-align:center;font-family:"Russo One",sans-serif;color:var(--lime);font-size:21px;line-height:29.5px;letter-spacing:1px}
.note{position:absolute;left:793px;top:735px;width:407px;height:120px;background:var(--note-bg);color:#f2f2f2;font-family:"Arimo",sans-serif;font-size:14px;line-height:18px;text-align:center;padding:9px 14px 0}
</style>
</head>
<body>

<section class="panel panel-left">
  <div class="dish"><span class="dish-name">Soy Chicken Satay Sauce (Spicy)</span><span class="dish-price">$15.90</span><span class="dish-desc">(Satay sauce with spices, cauliflowers, carrots, broccolis and celeries)</span></div>
  <div class="dish"><span class="dish-name">Lemon Roast Soy Chicken</span><span class="dish-price">$15.90</span><span class="dish-desc">(Lightly battered soy chicken drizzled in lemon sauce)</span></div>
  <div class="dish"><span class="dish-name">Soy Chicken on Hot Plate</span><span class="dish-price">$15.90</span><span class="dish-desc">(Special sauce combined with cauliflowers, carrots, capsicums, celeries and onions, served off a hot sizzling plate)</span></div>
  <div class="dish"><span class="dish-name">Shanton Soy Chicken</span><span class="dish-price">$15.90</span><span class="dish-desc">(Crispy soy chicken drizzled in Shanton sauce served with cucumber)</span></div>
  <div class="dish"><span class="dish-name">Soy Chicken Drumsticks &amp; Bok Choy</span><span class="dish-price">$15.90</span><span class="dish-desc">(Soy chicken drumstick tossed in a light sauce served with steamed bok choy)</span></div>
  <div class="dish"><span class="dish-name">Soy Chicken in Plum Sauce</span><span class="dish-price">$15.90</span><span class="dish-desc">(Crispy soy chiken drizzled in plum sauce)</span></div>

  <h2 class="section-band">Chef’s special</h2>

  <div class="dish"><span class="dish-name">Vietnamese Cannelloni</span><span class="dish-price">$14.90</span><span class="dish-desc">(Homemade rice paper roll with soy meat, mushroom puff and dried onion – served with special sauce)</span></div>
  <div class="dish"><span class="dish-name">Vietnamese Crepe</span><span class="dish-price">$15.90</span><span class="dish-desc">(Crepe with combination tofu, vegetable, bean and soy ham and served with fresh salad and special sauce</span></div>
  <div class="dish"><span class="dish-name">Vietnamese Rice Vermicelli Cake and B.B.Q Soy Meat</span><span class="dish-price">$15.90</span><span class="dish-desc">(Served with fresh salad and special sauce</span></div>
  <div class="dish"><span class="dish-name">Bo Tien Broken Rice</span><span class="dish-price">$14.90</span><span class="dish-desc">(Steamed broken rice with crab meat pate, shredded tofu and soy meat – Served with separate bowl of soup and special sauce)</span></div>
  <div class="dish"><span class="dish-name">Special Stew Soy Beef</span><span class="dish-price">$15.90</span></div>
  <div class="dish"><span class="dish-name">Small Bo Tien Sweet and Sour Soup</span><span class="dish-price">$16.90</span></div>
  <div class="dish"><span class="dish-name">Large Bo Tien Sweet and Sour Soup</span><span class="dish-price">$14.90</span><span class="dish-desc">(Banana flower, pineapples, tomatoes, celeries, bean shoots and basil leaves in sweet and sour soup)</span></div>
  <div class="dish"><span class="dish-name">Small Soy Seafood Sweet and Sour Soup</span><span class="dish-price">$15.90</span></div>
  <div class="dish"><span class="dish-name">Large Soy Seafood Sweet and Sour Soup</span><span class="dish-price">$17.90</span><span class="dish-desc">(Soy combination seafood, pineapples, tomatoes, celeries, bean shoots and basil leaves in sweet and sour soup)</span></div>
  <div class="dish"><span class="dish-name">Small Soy Beef Sweet &amp; Sour Soup (Spicy)</span><span class="dish-price">$15.90</span></div>
  <div class="dish"><span class="dish-name">Large Soy Beef Sweet &amp; Sour Soup (Spicy)</span><span class="dish-price">$17.90</span><span class="dish-desc">(Soy beef, pineapples, tomatoes, celeries, bean shoots and basil leaves in tom yum soup)</span></div>
  <div class="dish"><span class="dish-name">Sweet &amp; Sour Soy Squid</span><span class="dish-price">$15.90</span><span class="dish-desc">(Tomato and lemon sauce with pineapple, onions, carrots, cucumbers)</span></div>
  <div class="dish"><span class="dish-name">Stir Fried Soy Squid with Variety Vegetable</span><span class="dish-price">$16.90</span></div>
  <div class="dish"><span class="dish-name">Fried Soy Squid with Spicy Salt &amp; Chlli</span><span class="dish-price">$16.90</span><span class="dish-desc">(Soy Squid slightly dressed with salts, chilli &amp; served with onions, capsicums)</span></div>
</section>

<section class="panel panel-specials">
  <div class="dish"><span class="dish-name">Fried Soy Crab with Spicy Salt &amp; Chlli</span><span class="dish-price">$16.90</span></div>
  <div class="dish"><span class="dish-name">Eggplant in Claypot Sensation</span><span class="dish-price">$15.90</span></div>
  <div class="dish"><span class="dish-name">Roast Soy Duck</span><span class="dish-price">$15.90</span></div>
  <div class="dish"><span class="dish-name">Roast Soy Pork</span><span class="dish-price">$15.90</span></div>
  <div class="dish"><span class="dish-name">Soy Chicken in Black Bean Sauce</span><span class="dish-price">$15.90</span></div>
  <div class="dish"><span class="dish-name">Sizzling Mongolian Soy Lamb</span><span class="dish-price">$15.90</span></div>
  <div class="dish"><span class="dish-name">Small Stuffed Bitter Melon Soup</span><span class="dish-price">$14.90</span></div>
  <div class="dish"><span class="dish-name">Large Stuffed Bitter Melon Soup</span><span class="dish-price">$16.90</span></div>
  <div class="dish"><span class="dish-name">Bo Tien Eight Treasure (Combination Hot Pot)</span><span class="dish-price">$16.90</span><span class="dish-desc">(A special saucy stir fry with soy meats, tofu &amp; vegetables)</span></div>
  <div class="dish"><span class="dish-name">Grilled Soy Fish Sensation</span><span class="dish-price">$40.00</span><span class="dish-desc">(Served with rice paper, salad and savoury special sauce)</span></div>
  <div class="dish"><span class="dish-name">Small Vietnamese Fondue</span><span class="dish-price">$45.00</span></div>
  <div class="dish"><span class="dish-name">Large Vietnamese Fondue</span><span class="dish-price">$60.00</span><span class="dish-desc">(Traditional Vietnamese clear soup served with combination soy meats,vegetables and rice noodle)</span></div>
</section>

<section class="panel panel-rice">
  <h2 class="section-band">Rice</h2>
  <div class="dish"><span class="dish-name">Rice &amp; Veggie Combination</span><span class="dish-price">$12.00</span></div>
  <div class="dish"><span class="dish-name">Rice &amp; Satay Tofu</span><span class="dish-price">$12.00</span></div>
  <div class="dish"><span class="dish-name">Rice &amp; Soy Tuna in Tomato Sauce</span><span class="dish-price">$12.00</span></div>
  <div class="dish"><span class="dish-name">Small Combination Fried Rice</span><span class="dish-price">$6.90</span></div>
  <div class="dish"><span class="dish-name">Large Combination Fried Rice</span><span class="dish-price">$8.90</span></div>
  <div class="dish"><span class="dish-name">Steamed Rice (per person)</span><span class="dish-price">$2.50</span></div>
</section>

<section class="panel panel-banquet">
  <h2 class="section-band">Banquet</h2>
  <div class="banquet-set">
    <span class="set-price">$25.00 PER PERSON</span> <span style="font-weight:400;color:#1a1a1a;text-transform:none">(Minimum 4 persons)</span><br>
    Spring Rolls / Roast Soy Duck Wraps / Fresh Cold Rolls /<br>
    Sizzling Mongolian Soy Lamb /<br>
    Honey Soy Chicken / Buddha’s Feast /<br>
    Combination Fried Rice and Steamed Rice /<br>
    Four Season Fruits
  </div>
  <div class="banquet-set">
    <span class="set-price">$27.00 PER PERSON</span> <span style="font-weight:400;color:#1a1a1a;text-transform:none">(Minimum 4 persons)</span><br>
    Spring Rolls / Soy Chicken Satay Sticks / Curry Puffs /<br>
    Fresh Cold Rolls / Sizzling Mongolian Soy Lamb /<br>
    Braised Tofu and Vegetables with Cashew Nuts /<br>
    Egg Plant in Clay Pot /<br>
    Combination Fried Rice and Steamed Rice /<br>
    Four Season Fruits
  </div>
</section>

<header class="brand">
  <h1 class="brand-name">Bo Tien<br>Golden Vegetarian Cuisine</h1>
  <p class="brand-tag">Go Green</p>
</header>

<address class="info" style="font-style:normal">
  <p>Shop 7/12 Fernleaf St. Hollowbrook, ACT 2699</p>
  <p class="tagline">AUTHENTIC VIETNAMESE<br>VEGETARIAN CUISINE</p>
  <p>EFTPOS available (over $30.00)</p>
  <p>B.Y.O (bottled wine only)</p>
  <div class="gap"></div>
  <p>Phone: (02) 5550 1234</p>
  <p>Fax: (02) 5550 1235</p>
  <p>Website: www.botien-eatery.example.au</p>
  <p>Email: info@botien-eatery.example.au</p>
  <p class="gst">GST INCLUSIVE</p>
  <p>Lunch: Tue-Sun 11:30am - 2:30pm</p>
  <p>Dinner: Mon-Sun 5:30pm - 10:30pm</p>
</address>

<div class="promises">
  <p>NO EGG &nbsp;&nbsp; NO MSG</p>
  <p>NO CHOLESTEROL</p>
  <p>HEALTHY/ LOW FAT</p>
  <p>TASTY</p>
</div>

<aside class="note">
  All our dishes are vegetarian and prepared fresh without eggs, wine or MSG. All vegetarian imitation "meat" dishes like beef, pork, chicken, duck, fish, squid and shrimps are made of SOYBEAN proteins.<br>**Gluten Free or Nut Free is available on request**
</aside>

</body>
</html>
```